Website for "Bright Over Dusk Ltd" cleaning bsuiness

We require a website to expose our business to the local market. We want to provide background on who we are and what we do but in an easily digestible way. We clean domestic and commercial premises and want to provide a list of all of our services to potential customers. We operate out of Warrington in the UK.

We would like the website to be animated in some way so that the experience of using it is not dull or mundane. This website needs to be an extension of our company.

Target Market(s)

30 - 60 year olds for Domestic plus commercial clients

Industry/Entity Type

Cleaning Service

Coding

Coded - Design and coding required

Number of Pages Required

4 page

Font styles to use
Sans Serif

Colors
0455a3
3176b5
85acd3
cfdeed
ffffff
000000
1b1b1b
c8c8c8
757575

Requirements
Must have
• Logo which has been provided. Theme based around the logo and its colours. Simple layout to avoid confusion.
Nice to have
• Animations where possible to impress the customer.
Should not have
• any pictures of cleaning equipment, fairies, maids etc

```html
<!DOCTYPE html>
<html lang="en">
<head>
<meta charset="utf-8">
<title>Bright Over Dusk Ltd – Professional Cleaning Service</title>
<link href="https://fonts.googleapis.com/css2?family=Lato:ital,wght@0,400;0,700;0,900;1,400&family=Courgette&display=swap" rel="stylesheet">
<style>
:root{
  --brand:#0455a3;
  --brand-mid:#3176b5;
  --brand-soft:#85acd3;
  --brand-pale:#cfdeed;
  --white:#ffffff;
  --black:#000000;
  --ink:#1b1b1b;
  --grey-light:#c8c8c8;
  --grey:#757575;
}
*{box-sizing:border-box;margin:0;padding:0}
html,body{width:1200px;height:2727px;overflow:hidden;background:var(--white)}
body{font-family:'Lato',sans-serif;color:var(--ink)}
.page{position:relative;width:1200px;height:2727px;overflow:hidden}
.abs{position:absolute}
.script{font-family:'Courgette',cursive;color:var(--ink);font-weight:400}
.script b{color:var(--brand);font-weight:400}

/* top bar */
.top-bar{top:0;left:0;width:1200px;height:36px;background:var(--brand)}
.top-bar .contact{top:0;line-height:36px;color:var(--white);font-size:14px;display:flex;align-items:center;gap:7px}
.social{display:flex;gap:9px}
.social span{width:26px;height:26px;border:1.5px solid var(--brand-soft);border-radius:50%;display:block}
.top-bar .social{left:745px;top:5px}
.quote-btn{left:897px;top:0;width:168px;height:36px;background:var(--brand-mid);color:var(--white);font-size:15px;font-weight:700;display:flex;align-items:center;justify-content:center;gap:9px}

/* nav */
.main-nav{top:36px;left:0;width:1200px;height:92px;background:var(--white)}
.main-nav a{position:absolute;top:33px;font-size:17px;color:var(--ink);text-decoration:none}
.main-nav a.active{left:132px;top:26px;width:96px;height:34px;border:2px solid var(--brand);border-radius:18px;color:var(--brand);font-weight:700;text-align:center;line-height:30px}
.divider{position:absolute;top:38px;width:1px;height:18px;background:var(--grey-light)}
.brand-badge{left:519px;top:30px;width:180px;height:180px;border-radius:50%;background:var(--white);box-shadow:0 4px 10px rgba(0,0,0,.15);display:flex;align-items:center;justify-content:center;text-align:center;z-index:5}
.brand-badge span{font-weight:700;font-size:24px;line-height:1.15;color:var(--brand)}

/* hero */
.hero{top:127px;left:0;width:1200px;height:480px}
.hero-title{left:660px;top:185px;width:440px;text-align:center;font-family:'Courgette',cursive;color:var(--white);font-size:29px;line-height:42px;text-shadow:0 2px 4px rgba(0,0,0,.3)}
.hero-arrow{color:var(--white);font-size:40px;opacity:.8}

/* welcome */
.welcome{top:600px;left:0;width:1200px;height:342px;background:var(--brand-pale)}
.welcome h2{left:135px;top:60px;font-size:30px}
.welcome h2 .name{font-family:'Lato',sans-serif;font-weight:700;color:var(--brand);font-size:26px}
.welcome h2 small{font-size:14px;color:var(--ink)}
.rule{height:1px;background:var(--brand-soft)}
.welcome p{left:133px;top:135px;width:652px;font-size:14.5px;line-height:21.5px;color:var(--ink)}
.read-more{display:block;width:112px;height:27px;background:var(--brand);color:var(--white);font-size:13.5px;font-weight:700;line-height:27px;text-align:center}
.seal{left:887px;top:95px;width:136px;height:136px;border-radius:50%;border:4px solid var(--ink);opacity:.75}
.seal::after{content:"";position:absolute;inset:9px;border:2px solid var(--ink);border-radius:50%}

/* services */
.services{top:942px;left:0;width:1200px;height:503px;background:linear-gradient(180deg,#f3f7fb 0%,#e7eef6 55%,#dbe6f1 100%)}
.section-title{left:0;width:1200px;text-align:center;font-size:32px}
.service{width:260px}
.service h3{font-size:19.5px;font-weight:700;color:var(--brand)}
.service p{font-size:14px;line-height:20px;color:var(--ink);margin-top:6px}
.service.left{text-align:right}
.service-icon{width:74px;height:74px;border-radius:50%;background:var(--brand-mid);border:4px solid var(--brand);display:flex;align-items:center;justify-content:center}
.hub{left:486px;top:199px;width:228px;height:228px;border-radius:50%;background:var(--white);border:6px solid var(--brand);box-shadow:0 0 0 8px rgba(255,255,255,.8);display:flex;align-items:center;justify-content:center;text-align:center}
.hub span{font-weight:700;font-size:27px;line-height:1.15;color:var(--brand)}

/* how it works */
.how{top:1445px;left:0;width:1200px;height:524px;background:var(--brand-pale)}
.step{width:300px;height:360px;text-align:center}
.step-shape{position:absolute;left:55px;top:0;width:190px;height:188px;border-radius:14px;background:var(--brand-soft);opacity:.55}
.step-icon{position:absolute;left:115px;top:112px;width:70px;height:70px}
.step h3{position:absolute;top:206px;left:0;width:300px;font-size:20px;font-weight:700;color:var(--ink)}
.step p{position:absolute;top:244px;left:10px;width:280px;font-size:14px;line-height:22px;color:var(--ink)}
.step .read-more{position:absolute;top:308px;left:94px}

/* testimonials */
.testimonials{top:1969px;left:0;width:1200px;height:330px;background:var(--white)}
.client-photo{left:135px;top:165px;width:152px;height:152px;border-radius:50%;border:4px solid var(--brand);background:radial-gradient(circle at 50% 40%,#e9eef3 0%,#c9d4df 60%,#9fb1c4 100%)}
.quote{left:310px;top:168px;width:760px;font-size:14.5px;line-height:27px;font-style:italic;color:var(--ink)}
.quote .mark{font-family:'Courgette',cursive;font-size:38px;color:var(--grey-light);font-style:normal;line-height:0;vertical-align:-12px}
.client-name{left:312px;top:295px;font-size:17px;font-weight:700;color:var(--brand)}
.dots{left:1027px;top:2283px;display:flex;gap:6px}
.dots span{width:9px;height:9px;border-radius:50%;background:var(--grey-light)}
.dots span.on{background:var(--brand-mid);box-shadow:0 0 0 2px var(--white),0 0 0 3px var(--brand-mid)}

/* footer */
.footer{top:2418px;left:0;width:1200px;height:264px;background:var(--black);color:var(--white)}
.footer h4{font-size:16px;font-weight:700}
.footer .col-rule{height:1px;background:#333}
.footer ul{list-style:none;font-size:13.5px;line-height:29px}
.footer ul li::before{content:"› ";color:var(--grey)}
.footer .info{font-size:13.5px;line-height:20px;display:flex;gap:12px}
.map{left:607px;top:87px;width:205px;height:128px;background:linear-gradient(135deg,#e9e4d8 0%,#d9dfcf 45%,#c9d7e2 100%)}
.vrule{top:30px;width:1px;height:210px;background:#2b2b2b}
.footer-brand{left:858px;top:105px;width:220px;text-align:center;font-weight:700;font-size:28px;line-height:1.15;color:var(--grey-light)}
.bottom-bar{top:2682px;left:0;width:1200px;height:45px;background:var(--brand);color:var(--white);font-size:13px}
.bottom-bar .social span{border-color:var(--white);width:28px;height:28px}
</style>
</head>
<body>
<div class="page">

  <!-- top bar -->
  <div class="abs top-bar">
    <div class="abs contact" style="left:130px">
      <svg width="14" height="10" viewBox="0 0 14 10"><rect x="0.5" y="0.5" width="13" height="9" fill="none" stroke="#fff"/><path d="M0.5 0.5 L7 6 L13.5 0.5" fill="none" stroke="#fff"/></svg>
      info@brightoverduskcleaning.com
    </div>
    <div class="abs contact" style="left:380px">
      <svg width="13" height="13" viewBox="0 0 24 24"><path fill="#fff" d="M6.6 10.8a15 15 0 0 0 6.6 6.6l2.2-2.2c.3-.3.7-.4 1-.2 1.1.4 2.3.6 3.6.6.6 0 1 .4 1 1V20c0 .6-.4 1-1 1A17 17 0 0 1 3 4c0-.6.4-1 1-1h3.5c.6 0 1 .4 1 1 0 1.3.2 2.5.6 3.6.1.3 0 .7-.2 1z"/></svg>
      0123-555-0147
    </div>
    <div class="abs social"><span></span><span></span><span></span><span></span></div>
    <div class="abs quote-btn">
      <svg width="16" height="18" viewBox="0 0 16 18"><rect x="1" y="1" width="14" height="16" rx="1" fill="none" stroke="#fff" stroke-width="1.5"/><path d="M4 6h8M4 9h8M4 12h5" stroke="#fff" stroke-width="1.5"/></svg>
      Request A Quote
    </div>
  </div>

  <!-- navigation -->
  <nav class="abs main-nav">
    <a class="active" href="#">Home</a>
    <span class="divider" style="left:257px"></span>
    <a href="#" style="left:291px">About Us</a>
    <span class="divider" style="left:400px"></span>
    <a href="#" style="left:425px">Services</a>
    <a href="#" style="left:743px">Gallery</a>
    <span class="divider" style="left:822px"></span>
    <a href="#" style="left:842px">Testimonials</a>
    <span class="divider" style="left:958px"></span>
    <a href="#" style="left:977px">Contact Us</a>
  </nav>
  <div class="abs brand-badge"><span>Bright Over<br>Dusk Ltd</span></div>

  <!-- hero slider -->
  <section class="abs hero">
    <svg width="1200" height="480" viewBox="0 0 1200 480">
      <defs>
        <linearGradient id="homeTone" x1="0" y1="0" x2="1" y2="1">
          <stop offset="0" stop-color="#c9c2b2"/>
          <stop offset="0.5" stop-color="#a89f8c"/>
          <stop offset="1" stop-color="#5f7a48"/>
        </linearGradient>
        <linearGradient id="officeTone" x1="0" y1="0" x2="1" y2="1">
          <stop offset="0" stop-color="#6f9fdc"/>
          <stop offset="0.55" stop-color="#3f7fd0"/>
          <stop offset="1" stop-color="#2a63b3"/>
        </linearGradient>
      </defs>
      <g role="img" aria-label="Photograph of a detached family home with a gabled porch and garden shrubs">
        <polygon points="0,0 600,0 500,480 0,480" fill="url(#homeTone)"/>
      </g>
      <g role="img" aria-label="Photograph of a glass-fronted commercial office building tinted blue">
        <polygon points="600,0 1200,0 1200,480 500,480" fill="url(#officeTone)"/>
      </g>
      <path d="M0 400 Q600 520 1200 400 L1200 480 L0 480 Z" fill="#cfdeed"/>
    </svg>
    <div class="abs hero-title">Residential &amp; Commercial<br>Professional Cleaning Services</div>
    <div class="abs hero-arrow" style="left:55px;top:190px">‹</div>
    <div class="abs hero-arrow" style="left:1118px;top:190px">›</div>
  </section>

  <!-- welcome -->
  <section class="abs welcome">
    <h2 class="abs script">Welcome To <span class="name">Bright Over Dusk Ltd</span> <small>Professional Cleaning Service</small></h2>
    <div class="abs rule" style="left:135px;top:110px;width:660px"></div>
    <p class="abs">Lorem ipsum dolor sit amet, consectetuer adipiscing elit, sed diam nonummy nibh euismod tincidunt ut laoreet dolore magna aliquam erat volutpat. Ut wisi enim ad minim veniam, quis nostrud exerci tation ullamcorper suscipit lobortis nisl ut aliquip ex ea commodo consequat. Duis autem vel eum iriure dolor in hendrerit in vulputate velit esse molestie consequat, vel illum dolore eu feugiat nulla facilisis at vero eros et accumsan et iusto odio dignissim qui blandit praesent luptatum zzril delenit augue duis dolore te feugait nulla facilisi.</p>
    <a class="abs read-more" style="left:131px;top:280px">Read More</a>
    <div class="abs seal" aria-hidden="true"></div>
  </section>

  <!-- services -->
  <section class="abs services" role="region" aria-label="Our services">
    <h2 class="abs section-title script" style="top:48px">Our <b>Services</b></h2>
    <div class="abs rule" style="left:475px;top:95px;width:260px"></div>
    <svg class="abs" style="left:0;top:0" width="1200" height="503" viewBox="0 0 1200 503">
      <g fill="none" stroke="#0455a3" stroke-width="2">
        <polyline points="435,175 520,175 540,223"/>
        <line x1="435" y1="288" x2="486" y2="288"/>
        <polyline points="435,403 520,403 540,370"/>
        <polyline points="765,175 680,175 660,223"/>
        <line x1="765" y1="288" x2="714" y2="288"/>
        <polyline points="765,403 680,403 660,370"/>
      </g>
    </svg>
    <div class="abs hub"><span>Bright Over<br>Dusk Ltd</span></div>

    <div class="abs service left" style="left:83px;top:140px"><h3>Office Cleaning</h3><p>Duis autem vel eum iriure dolo<br>wisi enim ad minim veniam.</p></div>
    <div class="abs service left" style="left:83px;top:253px"><h3>Home Cleaning</h3><p>Duis autem vel eum iriure dolo<br>wisi enim ad minim veniam.</p></div>
    <div class="abs service left" style="left:83px;top:368px"><h3>Window Cleaning</h3><p>Duis autem vel eum iriure dolo<br>wisi enim ad minim veniam.</p></div>
    <div class="abs service" style="left:857px;top:140px"><h3>Builder Cleaning</h3><p>Duis autem vel eum iriure dolo<br>wisi enim ad minim veniam.</p></div>
    <div class="abs service" style="left:857px;top:253px"><h3>Floor Cleaning</h3><p>Duis autem vel eum iriure dolo<br>wisi enim ad minim veniam.</p></div>
    <div class="abs service" style="left:857px;top:368px"><h3>Other Cleaning</h3><p>Duis autem vel eum iriure dolo<br>wisi enim ad minim veniam.</p></div>

    <div class="abs service-icon" style="left:360px;top:138px"><svg width="32" height="32" viewBox="0 0 32 32" fill="none" stroke="#fff" stroke-width="2"><rect x="5" y="8" width="14" height="20"/><rect x="19" y="14" width="8" height="14"/><path d="M9 12h2M13 12h2M9 17h2M13 17h2M9 22h2M13 22h2"/></svg></div>
    <div class="abs service-icon" style="left:360px;top:251px"><svg width="32" height="32" viewBox="0 0 32 32" fill="#fff"><path d="M16 5 L4 15 h4 v11 h6 v-7 h4 v7 h6 V15 h4 Z"/></svg></div>
    <div class="abs service-icon" style="left:360px;top:366px"><svg width="32" height="32" viewBox="0 0 32 32" fill="none" stroke="#fff" stroke-width="2.5" stroke-linecap="round"><path d="M8 8 L22 8 M15 8 L15 14 L24 26"/></svg></div>
    <div class="abs service-icon" style="left:766px;top:138px"><svg width="34" height="30" viewBox="0 0 34 30" fill="#fff"><path d="M4 22 Q4 8 17 8 Q30 8 30 22 Z"/><rect x="2" y="22" width="30" height="4" rx="1"/></svg></div>
    <div class="abs service-icon" style="left:766px;top:251px"><svg width="32" height="32" viewBox="0 0 32 32" fill="#fff"><path d="M16 4 l2 4 4 1-4 1-2 4-2-4-4-1 4-1z"/><path d="M6 18 h20 l3 9 H3 Z"/></svg></div>
    <div class="abs service-icon" style="left:766px;top:366px"><svg width="32" height="32" viewBox="0 0 32 32" fill="none" stroke="#fff" stroke-width="2.5"><circle cx="19" cy="20" r="7"/><path d="M12 20 Q4 18 8 8"/></svg></div>
  </section>

  <!-- how it works -->
  <section class="abs how">
    <h2 class="abs section-title script" style="top:55px">How <b>It Works</b></h2>
    <div class="abs rule" style="left:458px;top:100px;width:290px"></div>

    <div class="abs step" style="left:122px;top:131px">
      <div class="step-shape" aria-hidden="true"></div>
      <svg class="step-icon" viewBox="0 0 80 80" fill="none" stroke="#3176b5" stroke-width="3"><rect x="22" y="14" width="36" height="52" rx="2"/><path d="M30 14 v22 l5-4 5 4 V14"/></svg>
      <h3>Book</h3>
      <p>Lorem ipsum dolor sit amet consectetuer adipiscing elit, sed diam nonummy</p>
      <a class="read-more">Read More</a>
    </div>
    <div class="abs step" style="left:450px;top:131px">
      <div class="step-shape" aria-hidden="true"></div>
      <svg class="step-icon" viewBox="0 0 80 80" fill="#3176b5"><rect x="32" y="10" width="16" height="8"/><path d="M48 12 h10 v4 H48z"/><path d="M30 26 h20 l4 12 v30 H26 V38 Z"/><circle cx="18" cy="16" r="2"/><circle cx="22" cy="26" r="2"/><circle cx="14" cy="30" r="2"/></svg>
      <h3>Clean</h3>
      <p>Lorem ipsum dolor sit amet consectetuer adipiscing elit, sed diam nonummy</p>
      <a class="read-more">Read More</a>
    </div>
    <div class="abs step" style="left:777px;top:131px">
      <div class="step-shape" aria-hidden="true"></div>
      <svg class="step-icon" viewBox="0 0 80 80" fill="none" stroke="#3176b5" stroke-width="3"><path d="M14 16 H66 L40 42 Z" fill="#3176b5"/><path d="M40 42 V68 M28 68 H52"/><circle cx="58" cy="12" r="5"/></svg>
      <h3>Relax</h3>
      <p>Lorem ipsum dolor sit amet consectetuer adipiscing elit, sed diam nonummy</p>
      <a class="read-more">Read More</a>
    </div>
  </section>

  <!-- testimonials -->
  <section class="abs testimonials">
    <h2 class="abs section-title script" style="top:47px">See What Clients <b>Have To Say About Us</b></h2>
    <div class="abs rule" style="left:255px;top:95px;width:700px"></div>
    <div class="abs client-photo" role="img" aria-label="Portrait photograph of a smiling client in shirt and tie"></div>
    <p class="abs quote"><span class="mark">“</span> Lorem ipsum dolor smit amet, consectetuer adipiscing elitmk, sed amet diam nonummy nibh euismodl tincidunt ut utmi laoreetmlhoi dolore magna aliquam erat volutpat. Ut wisi enim ad minim veniam, quis nostrud exer tationk lorem ullamcori permona suscipit lobortisk nisl utml mot aliqpi ex ea commodo consequat. Duis autem vel eumk iriurek dolor inj hendrerit inn vulputate velit esse molestiemo consequat. <span class="mark">”</span></p>
    <div class="abs client-name">- Mr. Aldric Penhale</div>
  </section>
  <div class="abs dots"><span class="on"></span><span></span><span></span></div>

  <!-- wave -->
  <svg class="abs" style="left:0;top:2295px" width="1200" height="130" viewBox="0 0 1200 130">
    <path d="M0 20 Q120 110 480 112 Q820 112 1200 50 L1200 130 L0 130 Z" fill="#0455a3"/>
    <path d="M0 40 Q160 122 520 122 Q860 120 1200 80 L1200 130 L0 130 Z" fill="#000"/>
  </svg>

  <!-- footer -->
  <footer class="abs footer">
    <h4 class="abs" style="left:133px;top:36px">Quick Links</h4>
    <div class="abs col-rule" style="left:133px;top:65px;width:125px"></div>
    <ul class="abs" style="left:133px;top:72px">
      <li>Home</li><li>About Us</li><li>Services</li><li>Gallery</li><li>Contact Us</li>
    </ul>
    <div class="abs vrule" style="left:285px"></div>

    <h4 class="abs" style="left:315px;top:36px">Contact Details</h4>
    <div class="abs col-rule" style="left:315px;top:65px;width:230px"></div>
    <div class="abs info" style="left:315px;top:80px">
      <svg width="12" height="16" viewBox="0 0 12 16"><path d="M6 0a6 6 0 0 0-6 6c0 4.5 6 10 6 10s6-5.5 6-10a6 6 0 0 0-6-6zm0 8.5A2.5 2.5 0 1 1 6 3.5a2.5 2.5 0 0 1 0 5z" fill="#fff"/></svg>
      <span>123 euismod cidun ut laok re<br>etmok laoreet dolmopi, magnak<br>aliquam-01234</span>
    </div>
    <div class="abs info" style="left:315px;top:152px;font-weight:700">
      <svg width="13" height="13" viewBox="0 0 24 24"><path fill="#fff" d="M6.6 10.8a15 15 0 0 0 6.6 6.6l2.2-2.2c.3-.3.7-.4 1-.2 1.1.4 2.3.6 3.6.6.6 0 1 .4 1 1V20c0 .6-.4 1-1 1A17 17 0 0 1 3 4c0-.6.4-1 1-1h3.5c.6 0 1 .4 1 1 0 1.3.2 2.5.6 3.6.1.3 0 .7-.2 1z"/></svg>
      0123-555-0147
    </div>
    <div class="abs info" style="left:315px;top:198px">
      <svg width="14" height="10" viewBox="0 0 14 10"><rect x="0.5" y="0.5" width="13" height="9" fill="none" stroke="#fff"/><path d="M0.5 0.5 L7 6 L13.5 0.5" fill="none" stroke="#fff"/></svg>
      info@brightoverduskcleaning.com
    </div>
    <div class="abs vrule" style="left:575px"></div>

    <h4 class="abs" style="left:607px;top:36px">Location Map</h4>
    <div class="abs col-rule" style="left:607px;top:65px;width:205px"></div>
    <div class="abs map" role="img" aria-label="Street map showing the office location"></div>
    <div class="abs vrule" style="left:840px"></div>

    <div class="abs footer-brand">Bright Over<br>Dusk Ltd</div>
  </footer>

  <div class="abs bottom-bar">
    <span class="abs" style="left:133px;top:14px">© 2016 Bright Over Dusk Cleaning Ltd. All Right Reserved.</span>
    <div class="abs social" style="left:918px;top:8px"><span></span><span></span><span></span><span></span></div>
  </div>

</div>
</body>
</html>
```